"The Plum Principle" Book Cover Design

Name of book: The Plum Principle

Tagline: Exploring 8 essential truths to living and loving more deeply.

Author: Rosalinda Ferrando-Vega

Size: 5in w x 8in h Paperback

This is the second book of 30 year old Entrepreneur, Author and Speaker. The book basically tells the story of her youth and immigrating to the United States at 14.

"The Plum Principle" name came about since she started selling figs outside her home in mexico city... Her family had a fig three in their backyard, and when she was about 6 she had the courage of starting her own business.

Here is the Book Description:
At some point in our lives, we all face the question: Does crisis and pain propel us forward or put our lives on hold? In this deeply intimate memoir, Rosalinda Ferrando Vega shares the eight hidden secrets—the fig factors as she calls them—of discovering true awareness and embracing life’s big sky possibilities, even amidst our greatest struggles.

The Plum Principle is an emotionally-charged story spanning two countries and three decades. Vega expertly takes our hand and invites us to walk with her. We begin in her homeland of Mexico as she recounts her mother’s unrelenting faith in giving birth to a little girl, the good that came from the arsonist’s flames devouring her childhood home and the life-changing discovery she encountered after watching her father walk away again and again with a bottle in his hand. Her immigration to the United States as a young teenager and the amazing medical discovery that both saved her life while nearly taking it away offer true inspiration that the human spirit dictates triumph in the lives of everyday people.

Vega clearly touches our hearts in this beautifully written, very personal memoir, showing us how to find more to every moment of living through love, awareness, forgiveness, gratitude and more. Each chapter is capped off with thought-provoking questions underscoring Vega’ real message: the answers to life’s greatest questions lie within each of us.
Updates

The author's favorite colors are Purple, Lime Green, and Black...  notice that Figs are also purple

Target Market(s)

Mostly women but men should also get interested in reading book

Industry/Entity Type

Medical

Requirements
Must have
• Title, tagline, and author's name;

The Plum Principle

Exploring the 8 essential truths to living and loving more deeply

Rosalinda Ferrando-Vega

```html
<!DOCTYPE html>
<html lang="en">
<head>
<meta charset="utf-8">
<title>The Plum Principle — Book Cover</title>
<link href="https://fonts.googleapis.com/css2?family=Marcellus&family=Share+Tech+Mono&display=swap" rel="stylesheet">
<style>
  :root {
    --ink: #0d0d0d;
    --photo-dark: #1c1c1c;
    --photo-mid: #6a6a6a;
    --photo-light: #b9b9b9;
    --plum: rgba(74, 52, 84, 0.86);
    --lime: #9ccd2a;
    --white: #f4f2f5;
  }
  * { margin: 0; padding: 0; box-sizing: border-box; }
  html, body { width: 750px; height: 1200px; overflow: hidden; background: var(--ink); }
  .cover {
    position: relative;
    width: 750px;
    height: 1200px;
    overflow: hidden;
  }
  .cover-photo {
    position: absolute;
    inset: 0;
    background:
      radial-gradient(ellipse 40% 30% at 12% 40%, var(--photo-light), transparent 70%),
      radial-gradient(ellipse 35% 25% at 88% 30%, var(--photo-mid), transparent 70%),
      radial-gradient(ellipse 45% 35% at 55% 35%, #3a3a3a, transparent 75%),
      radial-gradient(ellipse 40% 30% at 20% 85%, var(--photo-mid), transparent 70%),
      linear-gradient(160deg, #8a8a8a 0%, var(--photo-dark) 45%, #555 75%, var(--photo-dark) 100%);
  }
  .photo-credit {
    position: absolute;
    top: 18px;
    left: 16px;
    font-family: "Share Tech Mono", monospace;
    font-size: 10px;
    letter-spacing: 0.5px;
    color: var(--white);
  }
  .title-panel {
    position: absolute;
    left: 98px;
    top: 104px;
    width: 535px;
    height: 1000px;
    background: var(--plum);
  }
  .author {
    position: absolute;
    top: 140px;
    left: 98px;
    width: 535px;
    text-align: center;
    font-family: "Share Tech Mono", monospace;
    font-size: 24px;
    color: var(--lime);
  }
  .title {
    position: absolute;
    top: 592px;
    left: 60px;
    width: 611px;
    text-align: center;
    font-family: "Marcellus", serif;
    font-weight: 400;
    color: var(--white);
  }
  .title-article {
    display: flex;
    align-items: center;
    justify-content: center;
    gap: 14px;
    font-size: 62px;
    line-height: 1;
  }
  .title-article::before,
  .title-article::after {
    content: "";
    width: 40px;
    height: 3px;
    background: var(--white);
  }
  .title-word-main {
    display: block;
    font-size: 150px;
    line-height: 0.95;
    margin-top: 4px;
  }
  .title-word-second {
    display: block;
    font-size: 100px;
    line-height: 1;
    margin-top: -2px;
  }
  .divider {
    position: absolute;
    top: 948px;
    left: 0;
    width: 750px;
    height: 4px;
    background: var(--lime);
  }
  .tagline {
    position: absolute;
    top: 970px;
    left: 98px;
    width: 535px;
    display: flex;
    align-items: center;
    justify-content: center;
    gap: 8px;
    font-family: "Share Tech Mono", monospace;
    color: var(--white);
  }
  .tagline-brace {
    font-size: 58px;
    line-height: 1;
    color: var(--lime);
    font-weight: 400;
  }
  .tagline-text {
    font-size: 21px;
    line-height: 1.3;
    text-align: center;
  }
  .tagline-number { color: var(--lime); }
</style>
</head>
<body>
  <main class="cover">
    <div class="cover-photo" role="img" aria-label="Black and white close-up photograph of ripe figs filling the cover"></div>
    <p class="photo-credit">PHOTO CREDIT: MARA ELLISON</p>

    <div class="title-panel"></div>

    <p class="author">Rosalinda Ferrando-Vega</p>

    <h1 class="title">
      <span class="title-article">the</span>
      <span class="title-word-main">PLUM</span>
      <span class="title-word-second">PRINCIPLE</span>
    </h1>

    <div class="divider"></div>

    <p class="tagline">
      <span class="tagline-brace">{</span>
      <span class="tagline-text">Exploring the <span class="tagline-number">8</span> Essential Truths to<br>Living &amp; Loving More Deeply</span>
      <span class="tagline-brace">}</span>
    </p>
  </main>
</body>
</html>
```